Geschäftspapiere für Anbieter von Nahrungsergänzungsmitteln
Zielgruppe
Nahrungsergänzungsmittel
Menschen, die gesünder leben möchten und eventuell als Teampartner einsteigen möchten
Aufgabenstellung
Ich habe bereits ein Logo

```html
<!DOCTYPE html>
<html lang="de">
<head>
<meta charset="utf-8">
<title>Briefpapier Vitalweg</title>
<link href="https://fonts.googleapis.com/css2?family=Arimo:wght@400;700&family=Open+Sans:wght@400;600&display=swap" rel="stylesheet">
<style>
  :root{
    --backdrop:#e4e6e8;
    --paper:#ffffff;
    --mint:#52b89b;
    --teal-deep:#226e69;
    --ink:#3a3a3a;
    --ink-soft:#4a4a4a;
    --faint:#f3f3f3;
    --faint-text:#e6e6e6;
    --sign-blue:#dfe3f2;
  }
  *{box-sizing:border-box;margin:0;padding:0}
  html,body{width:1200px;height:945px;overflow:hidden;background:var(--backdrop)}
  .letterhead{
    position:absolute;left:280px;top:20px;width:640px;height:905px;
    background:var(--paper);overflow:hidden;
    box-shadow:0 2px 10px rgba(0,0,0,.15);
    font-family:"Arimo",Arial,sans-serif;color:var(--ink);
  }
  .band-top{position:absolute;left:0;top:0;width:640px;height:36px;background:var(--mint)}
  .band-bottom{position:absolute;left:0;bottom:0;width:640px;height:46px;background:var(--mint)}
  .rule-bottom{position:absolute;left:0;bottom:54px;width:640px;height:6px;background:var(--teal-deep)}
  .fold-mark{position:absolute;left:0;width:14px;height:1px;background:#bbb}
  .faint-mark{
    position:absolute;left:190px;top:520px;width:250px;height:250px;border-radius:50%;
    background:var(--faint);display:flex;align-items:center;justify-content:center;z-index:0;
  }
  .faint-mark span{font-size:28px;font-weight:700;color:var(--faint-text)}
  .sender-line{
    position:absolute;left:80px;top:150px;font-family:"Open Sans",sans-serif;
    font-size:6.5px;text-decoration:underline;color:var(--ink);
  }
  .brand{position:absolute;right:58px;top:120px;display:flex;align-items:center;gap:8px}
  .brand-dot{width:18px;height:18px;border-radius:50%;background:var(--mint)}
  .brand-name{font-size:17px;font-weight:700;color:var(--teal-deep)}
  .contact{
    position:absolute;left:470px;top:190px;padding-left:12px;
    border-left:1px solid var(--ink);font-style:normal;
    font-family:"Open Sans",sans-serif;font-size:8px;line-height:12px;color:var(--ink);
  }
  .contact-row{display:flex;align-items:center;gap:5px}
  .contact-row svg{width:8px;height:8px;flex:none}
  .letter-body{position:absolute;left:80px;top:300px;width:420px;font-size:10.5px;line-height:14px;color:var(--ink-soft);z-index:1}
  .salutation{margin-bottom:12px}
  .letter-body p{margin-bottom:12px;text-align:justify}
  .signature{width:200px;height:42px;margin:10px 0 6px;background:linear-gradient(90deg,var(--sign-blue),#eef0f8);border-radius:6px}
  .footer{position:absolute;font-family:"Open Sans",sans-serif;font-size:7.5px;line-height:11px;color:var(--ink);z-index:1}
  .footer-bank{left:60px;top:786px}
  .footer-tax{left:260px;top:797px;padding:4px 0 0 12px;border-left:1px solid var(--ink);height:36px}
</style>
</head>
<body>
<main class="letterhead">
  <div class="band-top" aria-hidden="true"></div>
  <div class="rule-bottom" aria-hidden="true"></div>
  <div class="band-bottom" aria-hidden="true"></div>

  <div class="fold-mark" style="top:300px"></div>
  <div class="fold-mark" style="top:452px"></div>

  <div class="faint-mark" aria-hidden="true"><span>Vitalweg</span></div>

  <div class="sender-line">Ulrike Brommel | 4812 Lindenbrunn | Mühlweg 7/2/5</div>

  <div class="brand"><span class="brand-dot"></span><span class="brand-name">Vitalweg</span></div>

  <address class="contact">
    <div>Ulrike Brommel</div>
    <div>4812 Lindenbrunn</div>
    <div>Mühlweg 7/2/5</div>
    <div class="contact-row">
      <svg viewBox="0 0 10 10"><path d="M2 1l2 2-1 1.5q1 2 2.5 2.5L7 6l2 2-1.5 1.5Q2 8 .5 2.5Z" fill="var(--mint)"/></svg>
      +43660 218 47 90
    </div>
    <div class="contact-row">
      <svg viewBox="0 0 10 10"><rect x="0.5" y="2" width="9" height="6" fill="var(--mint)"/><path d="M.5 2l4.5 3.5L9.5 2" stroke="#fff" fill="none" stroke-width=".8"/></svg>
      kontakt@vitalweg-post.at
    </div>
  </address>

  <section class="letter-body">
    <div class="salutation">Sehr geehrte Damen und Herren,</div>
    <p>In sollicitudin, metus et posuere blandit, erat dui bibendum eros, id vestibulum sem justo vel mauris. Ut tempor dolor ut justo vulputate, eu blandit libero faucibus. In laoreet, massa non ultricies tempor, est enim auctor mi, sit amet venenatis massa augue in justo. Praesent eu tincidunt diam. Maecenas id mi efficitur tellus interdum consectetur vel sed ante. Sed suscipit quis eros a fermentum. Curabitur ornare sit amet leo eu semper. Vestibulum pretium mi eu nisi. gadde.</p>
    <p>Sed nunc est, iaculis vel enim ut, fringilla commodo lorem. Pellentesque facilisis tempus lorem eget porttitor. Morbi accumsan, nulla accumsan mollis maximus, lectus diam venenatis odio, quis bibendum elit ex a arcu. Fusce turpis erat, euismod sit amet dolor eu, hendrerit rhoncus libero. Phasellus convallis, mi vel pharetra sollicitudin, nisi purus maximus est, nec lobortis dolor enim et augue. Vestibulum auctor mi sit amet leo auctor egestas. Pellentesque eget endrerit rhoncus dan.</p>
    <div>Mit freundlichen Grüßen</div>
    <div class="signature" role="img" aria-label="Handschriftliche Unterschrift von Ulrike Brommel"></div>
    <div>Ulrike Brommel</div>
  </section>

  <div class="footer footer-bank">
    Bankverbindung:<br>
    Talberg Kreditbank<br>
    BIC: TALBDE21XXX<br>
    IBAN: DE12 4507 3310 0462 0000 00
  </div>
  <div class="footer footer-tax">
    Steuernummer: 204/317/00000<br>
    Umsatzsteuer-ID-Nr.: DE 418273000
  </div>
</main>
</body>
</html>
```